A simple Facebook Ad (not Facebook Page) for weight loss surgery

It’s a simple ad in terms of the text.

The text should say:
Curious about weight loss surgery?
This 30 second quiz will tell you which procedure will suit you best

I'm open to variations in the text if it is thought to enhance the ad.

Targeted towards obese individuals who have been unable to lose weight with diet and exercise. My industry is weight loss surgery – webpage www.merivalebardsley.com.au. Clicking the ad leads to a quiz on my webpage relating to weight loss surgery. Most frequent users of this service are females (75%) between ages of 35 and 55 years.

Successful weight loss surgery can enable individuals who have been unable to lose weight to lose a substantial amount of the excess weight they are carrying to be healthier and happier.

```html
<!DOCTYPE html>
<html lang="en">
<head>
<meta charset="utf-8">
<title>Merivale Bardsley – Weight Loss Surgery Quiz Ad</title>
<link rel="stylesheet" href="https://fonts.googleapis.com/css2?family=Bebas+Neue&family=Poppins:wght@400;500;700&display=swap">
<style>
  :root {
    --teal: #16988c;
    --grey: #6d6e71;
    --grey-soft: #d9d9d9;
    --pattern: #f1f2f3;
    --paper: #ffffff;
  }
  * { margin: 0; padding: 0; box-sizing: border-box; }
  html, body { width: 1200px; height: 1200px; overflow: hidden; background: var(--paper); }
  .ad {
    position: relative;
    width: 1200px;
    height: 1200px;
    background: var(--paper);
    overflow: hidden;
    font-family: "Poppins", sans-serif;
  }
  .backdrop-pattern {
    position: absolute;
    left: 0; top: 0;
    width: 620px; height: 480px;
    background: radial-gradient(ellipse at 35% 35%, var(--pattern) 0%, rgba(241,242,243,0.5) 45%, rgba(255,255,255,0) 75%);
  }
  .figure-art {
    position: absolute;
    left: 117px; top: 198px;
    width: 390px; height: 1002px;
    border-radius: 160px 160px 0 0;
    background: linear-gradient(100deg, var(--teal) 0%, var(--teal) 62%, var(--grey-soft) 100%);
  }
  .brand {
    position: absolute;
    left: 712px; top: 58px;
    display: flex;
    align-items: center;
    gap: 18px;
  }
  .brand-dot {
    width: 64px; height: 64px;
    border-radius: 50%;
    background: var(--teal);
  }
  .brand-text { display: flex; flex-direction: column; }
  .brand-name {
    font-weight: 500;
    font-size: 31px;
    line-height: 1.1;
    letter-spacing: 1.5px;
    text-transform: uppercase;
    color: var(--teal);
  }
  .brand-role {
    font-weight: 400;
    font-size: 13.5px;
    letter-spacing: 1.6px;
    text-transform: uppercase;
    color: var(--grey);
  }
  .headline {
    position: absolute;
    left: 581px; top: 238px;
    font-family: "Bebas Neue", sans-serif;
    font-weight: 400;
    text-transform: uppercase;
  }
  .headline span { display: block; line-height: 0.84; }
  .headline .curious { font-size: 120px; color: var(--grey); letter-spacing: 1px; }
  .headline .about   { font-size: 72px;  color: var(--grey); margin-top: 6px; }
  .headline .weight  { font-size: 166px; color: var(--teal); margin-top: 6px; letter-spacing: 2px; }
  .headline .loss    { font-size: 166px; color: var(--teal); margin-top: -4px; letter-spacing: 2px; }
  .headline .surgery { font-size: 132px; color: var(--teal); margin-top: -2px; letter-spacing: 2px; }
  .offer {
    position: absolute;
    left: 583px; top: 850px;
    height: 200px;
    padding-left: 33px;
    border-left: 3px solid var(--grey);
    font-size: 40px;
    line-height: 52px;
    color: var(--grey);
    display: flex;
    align-items: center;
  }
  .offer strong { font-weight: 700; }
  .offer .highlight { color: var(--teal); }
</style>
</head>
<body>
  <main class="ad">
    <div class="backdrop-pattern" role="img" aria-label="Faint hexagonal medical cross pattern"></div>
    <div class="figure-art" role="img" aria-label="Silhouette of a slim woman in teal in front of a larger grey silhouette, showing weight loss"></div>

    <header class="brand">
      <div class="brand-dot"></div>
      <div class="brand-text">
        <span class="brand-name">Merivale Bardsley</span>
        <span class="brand-role">General, Upper GI &amp; Bariatric Surgeon</span>
      </div>
    </header>

    <h1 class="headline">
      <span class="curious">Curious</span>
      <span class="about">About</span>
      <span class="weight">Weight</span>
      <span class="loss">Loss</span>
      <span class="surgery">Surgery?</span>
    </h1>

    <p class="offer">
      <span>This <strong>30 second quiz</strong><br>will tell you<br><span class="highlight">which procedure will<br>suit you best</span></span>
    </p>
  </main>
</body>
</html>
```